New Podcast focussing on non-mainstream interventions for guidance needs podcast art

I need an exquisite piece of podcast art work for the launch of my new podcast 'Past the Hollow'. This podcast explores unorthodox, esoteric and unconventional methods to find peace, clarity and direction in life. Topics include family Constellations Systems, Psychedelics, Equine Therapy and Floatation to name a few. A teaser has been posted on Brevlo with a strong response. The audience is primarily midlifers or those in a career/personal crisis of direction. It's meant to comfort, inform and empower and offer other ways rather than mainstream to work out what to do with your life. The file shared with you shows the pic used on Brevlo as it's illustrating the idea of illumination. You can use it or not, and whilst I am ex-Military, I don't want the cover to convey an overly military influence. I'd like 'Past the Hollow' to feature on the art work and my name, Margot Pennick. I'd like inspiration, creativity, and the idea of hope conveyed as well as clarity and courage. Whilst the podcast is about finding your direction please do no use compass images or cross road images as that is too obvious.
Hope that all helps. Looking forward to your ideas.

```html
<!DOCTYPE html>
<html lang="en">
<head>
<meta charset="UTF-8">
<title>Past the Hollow — Podcast Cover</title>
<link rel="stylesheet" href="https://fonts.googleapis.com/css2?family=Pacifico&family=Poppins:wght@500;600;700&display=swap">
<style>
  :root {
    --title-gold: #ffc857;
    --title-white: #fff6f2;
    --title-dark: #2e0c07;
    --host-white: #ffffff;
    --sky-top: #3a0806;
    --sky-red: #8e1a10;
    --sky-coral: #dc4a3c;
    --sky-glow: #f27a5e;
    --horizon-amber: #e0702e;
    --shore-rust: #9a3a16;
    --shore-dark: #2a0c08;
    --sun-core: #fff4e0;
  }
  html, body {
    margin: 0;
    padding: 0;
    width: 1200px;
    height: 1200px;
    overflow: hidden;
    background: var(--shore-dark);
  }
  .cover {
    position: relative;
    width: 1200px;
    height: 1200px;
    overflow: hidden;
    font-family: "Poppins", sans-serif;
  }
  .cover-photo {
    position: absolute;
    inset: 0;
    width: 1200px;
    height: 1200px;
  }
  .title-line {
    position: absolute;
    left: 0;
    width: 100%;
    margin: 0;
    text-align: center;
    line-height: 1;
    font-family: "Poppins", sans-serif;
  }
  .title-past {
    top: 50px;
    font-size: 225px;
    font-weight: 600;
    color: var(--title-gold);
    letter-spacing: -2px;
  }
  .title-the {
    top: 250px;
    font-size: 79px;
    font-weight: 600;
    color: var(--title-white);
  }
  .title-hollow {
    top: 305px;
    font-size: 210px;
    font-weight: 600;
    color: var(--title-dark);
    letter-spacing: -2px;
  }
  .host-with {
    position: absolute;
    left: 124px;
    top: 905px;
    margin: 0;
    font-family: "Pacifico", cursive;
    font-size: 40px;
    line-height: 1;
    color: var(--title-gold);
  }
  .host-name {
    position: absolute;
    left: 124px;
    top: 987px;
    margin: 0;
    font-size: 64px;
    font-weight: 500;
    line-height: 1;
    letter-spacing: 3px;
    color: var(--host-white);
  }
</style>
</head>
<body>
  <main class="cover">
    <svg class="cover-photo" viewBox="0 0 1200 1200" role="img" aria-label="Photograph of a lone figure kneeling on a rocky shore, silhouetted against a blazing red and orange sunset over the sea, with a large glowing sun breaking through clouds">
      <defs>
        <linearGradient id="sky" x1="0" y1="0" x2="0" y2="1">
          <stop offset="0" stop-color="var(--sky-top)"/>
          <stop offset="0.14" stop-color="var(--sky-red)"/>
          <stop offset="0.34" stop-color="var(--sky-coral)"/>
          <stop offset="0.5" stop-color="var(--sky-glow)"/>
          <stop offset="0.66" stop-color="var(--horizon-amber)"/>
          <stop offset="0.76" stop-color="var(--shore-rust)"/>
          <stop offset="0.86" stop-color="#4a140a"/>
          <stop offset="1" stop-color="var(--shore-dark)"/>
        </linearGradient>
        <radialGradient id="sun" cx="712" cy="620" r="360" gradientUnits="userSpaceOnUse">
          <stop offset="0" stop-color="var(--sun-core)" stop-opacity="1"/>
          <stop offset="0.25" stop-color="#ffd9a8" stop-opacity="0.85"/>
          <stop offset="0.6" stop-color="#f5905a" stop-opacity="0.35"/>
          <stop offset="1" stop-color="#f5905a" stop-opacity="0"/>
        </radialGradient>
      </defs>
      <rect width="1200" height="1200" fill="url(#sky)"/>
      <rect width="1200" height="1200" fill="url(#sun)"/>
    </svg>

    <h1 class="title">
      <span class="title-line title-past">PAST</span>
      <span class="title-line title-the">THE</span>
      <span class="title-line title-hollow">HOLLOW</span>
    </h1>

    <p class="host-with">with</p>
    <p class="host-name">MARGOT PENNICK</p>
  </main>
</body>
</html>
```